Landingpage design

We need a landingpage for a chatterloop add campaign. We sell socks made of bamboo in super quality. Our customers loves us, and we have a 5 heart rating at opinivo.com.

We want to create a add campaign targeted new customers, and the offer is that they can buy 1 pair of bamboo socks as a test, for only 20 DKK (2,7 Euro) including shipment. Our webpage is www.lintora.dk, landingpage should be built i Pagmoro, a wysiwyg editor. based on their template. like:
https://lintora.pagmoro.com/13844-sales-page
https://lintora.pagmoro.com/13696-sales-page
https://lintora.pagmoro.com/13845-sales-page

You don't have to follow the templates 100% if you have better ideas. We have an account for snapquarry, so please get stockphotos from here.

Bamboo socks has a lot of great selling points, you can see a good desciption here:
https://tovelin.com/us/why-bamboo

We expect you to have experience in landingpage design, and expect to end up with 2 landingpages we can splittest on.

This is the first of a number of landingpages we need in the future, so for the right person there will be plenty of more work.

Target Market(s)

Denmark

Industry/Entity Type

E-Commerce

Number of Pages Required

2 page

Colors

Designer to choose colors to be used in the design.

Requirements
Must have
• A great selling page, showing all the great things with bamboo socks. It should be supplied with good packshots from snapquarry.com

```html
<!DOCTYPE html>
<html lang="en">
<head>
<meta charset="utf-8">
<title>Lintora – Bamboo Socks</title>
<link href="https://fonts.googleapis.com/css2?family=Roboto:wght@300;400;500;700&display=swap" rel="stylesheet">
<style>
:root{
  --green:#3aae86;
  --green-light:#3ae0a4;
  --ink:#555a5e;
  --muted:#8c9093;
  --paper:#f1f1f1;
  --white:#ffffff;
  --card:#f2f2f2;
  --rule:#d9dde0;
}
*{margin:0;padding:0;box-sizing:border-box}
html,body{width:1200px;height:2604px;overflow:hidden}
body{position:relative;font-family:'Roboto',sans-serif;color:var(--ink);background:var(--white)}
.abs{position:absolute}

/* header */
.site-header{left:0;top:0;width:1200px;height:70px;background:var(--white)}
.brand{left:135px;top:17px;display:flex;align-items:center;gap:12px}
.brand-mark{width:36px;height:36px;background:#222;}
.brand-name{font-size:17px;font-weight:500;color:#222;line-height:1.15}
.brand-name small{display:block;font-size:13px;font-weight:400}
.nav a{position:absolute;top:27px;font-size:13px;color:var(--ink);text-decoration:none;letter-spacing:.3px}
.nav a.active{border-bottom:1px solid var(--ink);padding-bottom:4px}
.btn{display:flex;align-items:center;justify-content:center;font-size:13px;font-weight:500;letter-spacing:.5px;text-decoration:none}
.btn-solid{background:var(--green);color:var(--white)}
.btn-outline{border:1.5px solid var(--green);color:var(--green);gap:10px}
.nav-buy{left:908px;top:21px;width:158px;height:28px}

/* hero */
.hero{left:0;top:70px;width:1200px;height:475px;background:var(--paper)}
.hero-title{left:135px;top:96px;width:700px;font-size:43px;font-weight:500;line-height:52px;color:var(--ink)}
.hero-list{left:135px;top:218px;list-style:none}
.hero-list li{display:flex;align-items:center;gap:14px;font-size:15.5px;color:#6d7175;height:28px}
.hero-buy{left:135px;top:321px;width:192px;height:35px}
.hero-video{left:346px;top:321px;width:192px;height:35px}
.hero-note{left:135px;top:366px;font-size:12px;color:var(--muted)}
.hero-photo{left:795px;top:26px;width:288px;height:449px;background:linear-gradient(180deg,#e6dcd4 0%,#2f8f6c 40%,#1f7a5a 100%);border-radius:120px 120px 0 0}

/* why */
.why{left:0;top:545px;width:1200px;height:510px;background:linear-gradient(180deg,#38ae86 0%,#3ae0a4 100%);color:var(--white)}
.why-title{left:0;top:97px;width:1200px;text-align:center;font-size:34px;font-weight:400}
.why-rule{left:547px;top:141px;width:108px;height:1.5px;background:var(--white)}
.why-lead{left:0;top:160px;width:1200px;text-align:center;font-size:16px;line-height:26px;font-weight:500}
.why-cards{left:135px;top:267px;width:931px;height:138px;display:flex;background:var(--card)}
.why-card{flex:1;border-right:1px solid var(--rule);text-align:center;padding:26px 20px 0}
.why-card:last-child{border-right:none}
.why-card h3{font-size:19px;font-weight:400;color:var(--ink);margin-bottom:10px}
.why-card p{font-size:11.5px;line-height:17px;color:var(--muted)}

/* features */
.feature-photo{width:421px;height:245px}
.feature-title{font-size:30px;font-weight:500;color:var(--ink)}
.feature-text{width:460px;font-size:15px;line-height:26px;color:var(--muted)}

/* promo */
.promo{left:0;top:2215px;width:1200px;height:389px;background:var(--paper);border-bottom:3px solid #9fd6ea}
.promo-figure{left:0;top:60px;width:1200px;text-align:center;font-size:84px;font-weight:700;color:var(--green);line-height:96px}
.promo-title{left:0;top:160px;width:1200px;text-align:center;font-size:26px;font-weight:500;line-height:33px;color:var(--ink)}
.promo-buy{left:503px;top:254px;width:192px;height:35px}
.promo-note{left:0;top:300px;width:1200px;text-align:center;font-size:12px;color:var(--muted)}
</style>
</head>
<body>

<header class="abs site-header">
  <div class="abs brand">
    <span class="brand-mark"></span>
    <span class="brand-name">Lintora<small>Basics i bambus - lige til og enkelt</small></span>
  </div>
  <nav class="nav">
    <a href="#" class="active" style="left:486px">HOME</a>
    <a href="#" style="left:564px">WHY BAMBOO</a>
    <a href="#" style="left:695px">ABOUT US</a>
    <a href="#" style="left:800px">REVIEWS</a>
  </nav>
  <a href="#" class="abs btn btn-solid nav-buy">BUY NOW</a>
</header>

<section class="abs hero">
  <h1 class="abs hero-title">Enjoy Your First Pair of Bamboo Socks for Only 20 PKK</h1>
  <ul class="abs hero-list">
    <li><svg width="16" height="12" viewBox="0 0 16 12"><path d="M1 6l4.5 4.5L15 1" fill="none" stroke="#3aae86" stroke-width="2"/></svg>We have been working on textile for more than 10 years</li>
    <li><svg width="16" height="12" viewBox="0 0 16 12"><path d="M1 6l4.5 4.5L15 1" fill="none" stroke="#3aae86" stroke-width="2"/></svg>All products meet our high quality standards</li>
    <li><svg width="16" height="12" viewBox="0 0 16 12"><path d="M1 6l4.5 4.5L15 1" fill="none" stroke="#3aae86" stroke-width="2"/></svg>Our customers loves us, and we have a 5 stars rating at opinivo.com</li>
  </ul>
  <a href="#" class="abs btn btn-solid hero-buy">BUY NOW</a>
  <a href="#" class="abs btn btn-outline hero-video"><svg width="10" height="12" viewBox="0 0 10 12"><path d="M0 0l10 6-10 6z" fill="#3aae86"/></svg>WATCH VIDEO</a>
  <p class="abs hero-note">Shipment included</p>
  <div class="abs hero-photo" role="img" aria-label="Model wearing a green bamboo tank top and briefs"></div>
</section>

<section class="abs why">
  <h2 class="abs why-title">Why Bamboo Clothing?</h2>
  <span class="abs why-rule"></span>
  <p class="abs why-lead">It was only in 2011 that the University of Hanvale discovered how you can make fabric<br>from bamboo stems. Now bamboo has the potential to become the textile of the future.</p>
  <div class="abs why-cards">
    <div class="why-card"><h3>Comfortable</h3><p>Bamboo fabric breathes making you comfortable in garments made in this.</p></div>
    <div class="why-card"><h3>Eco-friendly</h3><p>Bamboo is a very fast-growing, tropical forest product, which does not require the use of pesticides</p></div>
    <div class="why-card"><h3>Exquisitely soft</h3><p>The moment you wear it next to your skin you will notice the difference between other fabrics.</p></div>
    <div class="why-card"><h3>Thermo-control</h3><p>Bamboo fabric is warm, thanks to its hollow microfibre, yet is also breathable.</p></div>
  </div>
</section>

<div class="abs feature-photo" style="left:135px;top:1170px;background:linear-gradient(135deg,#2a2a2c 0%,#7d7f82 55%,#8a6378 100%)" role="img" aria-label="Grey argyle bamboo socks beside black leather shoes"></div>
<h2 class="abs feature-title" style="left:610px;top:1214px">Strong Material</h2>
<p class="abs feature-text" style="left:610px;top:1264px">Bamboo fabric is lightweight yet strong. The natural processing of verdaxa bamboo allows the fibre to remain strong to produce an extremely high quality product. This process gives a material that is very durable.</p>

<h2 class="abs feature-title" style="left:133px;top:1556px">Completely Clean</h2>
<p class="abs feature-text" style="left:135px;top:1606px">Bamboo fibers doesnot under go much chemical processing to make the fabric ; so you can easily wear it without causing any allergic irritation to the skin that is more prevalent with heavily processes fabrics.</p>
<div class="abs feature-photo" style="left:645px;top:1513px;background:linear-gradient(135deg,#3b4550 0%,#1e2228 50%,#c9a99a 100%)" role="img" aria-label="Person in dark shirt and light underwear sitting on a bench"></div>

<div class="abs feature-photo" style="left:135px;top:1855px;background:linear-gradient(135deg,#3f4246 0%,#6d7074 45%,#d8d6d2 100%)" role="img" aria-label="Pair of light grey ribbed bamboo socks on dark stone"></div>
<h2 class="abs feature-title" style="left:610px;top:1910px">Water Absorbent</h2>
<p class="abs feature-text" style="left:610px;top:1960px">Bamboo fibers are water absobent. So if you live in a humid environment this is the fabric for you. Think of the sweat it will absorb and evaporate out of your body.</p>

<section class="abs promo">
  <p class="abs promo-figure">-90%</p>
  <h2 class="abs promo-title">Get Your First Pair of Socks With<br>an Exclusive Discount</h2>
  <a href="#" class="abs btn btn-solid promo-buy">BUY NOW</a>
  <p class="abs promo-note">Shipment included</p>
</section>

</body>
</html>
```